The Quiet Orchard Method - 12-Week Harvest Ledger

I am finishing a book that is designed to be super hands on. It steps he reader through a 90 day roadmap - as a pick up, put down action diary style piece. The foundational idea is to speak about the Quiet Orchard Method. With a cost of living crisis this is designed to create action and understanding. I am looking for a cover for the ebook that will blow away the competitors in the category. I want it to be bright, attractive and leap off the lumeno page - appeal to a wide audience. I have pasted in a file with the best selling books in the category so you can see what's working.

```html
<!DOCTYPE html>
<html lang="en">
<head>
<meta charset="utf-8">
<title>The Quiet Orchard Method – 12-Week Harvest Ledger</title>
<link rel="stylesheet" href="https://fonts.googleapis.com/css2?family=Big+Shoulders+Display:wght@900&family=Poppins:wght@600;700;800&display=swap">
<style>
  :root {
    --cover-bg: #efe3ee;
    --author-ink: #2e2a2c;
    --title-soft: #b68bba;
    --title-deep: #7a4878;
    --title-light: #b487b6;
    --subtitle-ink: #4f2f4f;
    --art-light: #dfe0cf;
    --art-mid: #b9c0ad;
  }
  * { margin: 0; padding: 0; box-sizing: border-box; }
  html, body { width: 804px; height: 1200px; overflow: hidden; }
  body { background: var(--cover-bg); }
  .cover {
    position: relative;
    width: 804px;
    height: 1200px;
    background: var(--cover-bg);
    overflow: hidden;
  }
  .author {
    position: absolute;
    top: 48px;
    left: 0;
    width: 100%;
    text-align: center;
    font-family: "Poppins", sans-serif;
    font-weight: 700;
    font-size: 33px;
    letter-spacing: 4.5px;
    color: var(--author-ink);
  }
  .title-art {
    position: absolute;
    inset: 0;
    width: 804px;
    height: 1200px;
  }
  .title-lead {
    font-family: "Poppins", sans-serif;
    font-weight: 800;
    font-size: 66px;
    fill: var(--title-soft);
  }
  .title-word {
    font-family: "Big Shoulders Display", sans-serif;
    font-weight: 900;
    font-size: 236px;
  }
  .title-word--deep { fill: var(--title-deep); }
  .title-word--light { fill: var(--title-light); }
  .cover-art {
    position: absolute;
    left: 159px;
    top: 660px;
    width: 476px;
    height: 368px;
    border-radius: 6px;
    background: radial-gradient(ellipse at 50% 45%, var(--art-light) 0%, var(--art-mid) 100%);
  }
  .subtitle {
    position: absolute;
    top: 1046px;
    left: 0;
    width: 100%;
    text-align: center;
    font-family: "Poppins", sans-serif;
    font-weight: 700;
    font-size: 46px;
    line-height: 48px;
    color: var(--subtitle-ink);
  }
</style>
</head>
<body>
  <main class="cover">
    <p class="author">DANA WHITCOMBE</p>

    <svg class="title-art" viewBox="0 0 804 1200" aria-label="The Quiet Orchard Method">
      <text class="title-lead" x="402" y="196" text-anchor="middle">THE QUIET</text>
      <text class="title-word title-word--deep" x="53" y="441" textLength="696" lengthAdjust="spacingAndGlyphs">ORCHARD</text>
      <text class="title-word title-word--light" x="53" y="652" textLength="693" lengthAdjust="spacingAndGlyphs">METHOD</text>
    </svg>

    <div class="cover-art" role="img" aria-label="Cover artwork: a brain made of folded banknotes standing on a slim stem"></div>

    <p class="subtitle">12-WEEK<br>HARVEST LEDGER</p>
  </main>
</body>
</html>
```